WordPress Website for Accounting Firm

I have attached an excel sheet showing what i need done for my accounting website. Currently i have a WP website but its not live and do not like it. I can give a link if that will help. Total pages is around 12. I can buy and supply the images but have provided indication of what i want in the excel. I will need the designer to do the coding to make the website fully functional. I want a clean look and attractive. Don't want too dark colors. Once i like the landing page, i will need the designer to code code the website. Just want to look first. I will provide the logo file and put the contents myself. Just put dummy contents for now to show how it will look.
Can you please use the attached images so i can see how nit will look on the coverage as an option. These are from pixelharbor
903516284
475120968
2067391145
1830647729
Currently there are only 2 provided by myself as Photo 1 and Photo 2
Many Thanks!
Accounting and Finance
5+ page

```html
<!DOCTYPE html>
<html lang="en">
<head>
<meta charset="utf-8">
<title>Ledgerline Advisory</title>
<link rel="stylesheet" href="https://fonts.googleapis.com/css2?family=Righteous&family=Montserrat:wght@400;500;600&display=swap">
<style>
:root{
  --green:#4c9a40;
  --green-light:#6cc04a;
  --taupe:#7b736a;
  --ink:#2b2b2b;
  --text:#555;
  --soft:#f3f3f3;
  --white:#fff;
  --star:#f2a51a;
  --partner:#e3e3e3;
}
*{box-sizing:border-box;margin:0;padding:0}
html,body{width:1200px;height:3976px;overflow:hidden}
body{position:relative;background:var(--white);font-family:"Montserrat",sans-serif;color:var(--text)}
.abs{position:absolute}
.display{font-family:"Righteous",sans-serif;letter-spacing:2px;color:var(--ink);text-transform:uppercase;font-weight:400}
.btn{position:absolute;background:var(--green);color:var(--white);border-radius:22px;display:flex;align-items:center;justify-content:center;font-size:13px}

/* header */
.brand{left:74px;top:46px;display:flex;align-items:center;gap:12px}
.brand-mark{width:22px;height:22px;background:var(--green)}
.brand-name{font-size:19px;color:#666;font-weight:500;letter-spacing:1px}
.partner{top:34px;width:52px;height:52px;border-radius:6px;background:var(--partner)}
.nav{left:0;top:134px;width:1200px;height:47px;background:var(--green);display:flex}
.nav a{flex:1;color:var(--white);font-size:14px;display:flex;align-items:center;justify-content:center;text-decoration:none;position:relative}
.nav a.active{background:var(--taupe);flex:0 0 155px;margin-left:77px}
.nav a+a:not(.active)::before{content:"";position:absolute;left:0;top:16px;height:15px;border-left:1px solid rgba(255,255,255,.4)}
.nav a.active+a::before{display:none}

/* hero */
.hero{left:0;top:181px;width:1200px;height:700px;background:linear-gradient(180deg,#7f9ab1 0%,#a9bccb 35%,#c9c3a9 58%,#37506a 72%,#5a3a2a 100%)}
.hero-title{left:113px;top:405px;width:600px;font-size:46px;line-height:52px;color:var(--white)}
.hero-title span{color:var(--green-light)}
.hero-lead{left:113px;top:515px;width:480px;font-size:18px;color:var(--white);line-height:24px}

/* about */
.title-rule{position:absolute;height:2px;background:var(--green);width:60px}
.about-copy{left:200px;width:800px;text-align:center;font-size:13px;line-height:22.5px}

/* solution */
.solution-band{left:0;top:1331px;width:1200px;height:648px;background:var(--soft)}
.card{position:absolute;top:1447px;height:461px;background:var(--white)}
.card .photo{height:203px}
.card .icon{position:absolute;left:30px;top:186px;width:50px;height:50px;border-radius:50%;background:var(--white);display:flex;align-items:center;justify-content:center}
.card h3{position:absolute;left:24px;top:242px;font-size:18px}
.card .rule{position:absolute;left:24px;top:282px;width:46px;height:2px;background:#999}
.card ul{position:absolute;left:24px;top:298px;list-style:none;font-size:15px;color:var(--ink);line-height:25px}
.card li::before{content:"•";margin-right:12px;font-size:18px}

/* why */
.why{left:0;top:1979px;width:1200px;height:566px;background:var(--green)}
.why-title{left:74px;top:2072px;font-size:36px;color:var(--white)}
.why-list{left:74px;top:2142px;width:520px;list-style:none;color:var(--white);font-size:15px;line-height:20px}
.why-list li{position:relative;padding-left:38px}
.why-list li svg{position:absolute;left:0;top:3px}

/* testimonials */
.quote-card{position:absolute;top:2738px;width:304px;height:291px;background:var(--white);box-shadow:0 2px 12px rgba(0,0,0,.12);text-align:center}
.quote-mark{position:absolute;left:22px;top:-26px;width:48px;height:48px;border-radius:50%;background:var(--green);color:var(--white);font-family:"Righteous",sans-serif;font-size:28px;display:flex;align-items:center;justify-content:center}
.avatar{width:100px;height:100px;border-radius:50%;margin:22px auto 0;background:linear-gradient(160deg,#c9d6e0,#5d6f80)}
.quote-card h4{margin-top:12px;font-size:17px;font-weight:500;letter-spacing:1.5px;color:var(--ink)}
.quote-card .role{color:var(--green);font-size:15px;margin-top:2px}
.quote-card p{font-size:12px;line-height:15px;margin:12px 24px 0}
.stars{color:var(--star);font-size:13px;letter-spacing:3px;margin-top:10px}

/* industries */
.ind{position:absolute;display:flex;align-items:center;gap:12px;font-family:"Righteous",sans-serif;font-size:16px;letter-spacing:1.5px;color:#444;line-height:18px;text-transform:uppercase}

/* footer */
.footer h5{position:absolute;font-size:14px;color:var(--white);font-weight:500}
.footer .hr{position:absolute;width:40px;height:1px;background:var(--white)}
.footer ul{position:absolute;list-style:none;color:var(--white);font-size:14px;line-height:22.5px}
.footer li::before{content:">";margin-right:10px}
.contact{position:absolute;color:var(--white);font-size:13px;line-height:26px}
.social{width:30px;height:30px;border-radius:50%;background:var(--ink);display:inline-block;margin-left:7px}
.social.g{background:var(--green)}
</style>
</head>
<body>

<!-- header -->
<div class="abs brand"><span class="brand-mark"></span><span class="brand-name">LEDGERLINE ADVISORY</span></div>
<div class="abs partner" style="left:1000px"></div>
<div class="abs partner" style="left:1062px"></div>

<nav class="abs nav">
  <a class="active">Home</a><a>About us</a><a>Solution</a><a>Clients</a><a>Contact us</a><a>Clients Resource</a>
</nav>

<!-- hero -->
<section class="abs hero" role="img" aria-label="Photograph of a climber helping another up a seaside rock at sunrise"></section>
<h1 class="abs display hero-title">Don't take<br><span>our world</span> for it</h1>
<p class="abs hero-lead">Lorem Ipsum is simply dummy text of the printing and typesetting industry.</p>
<div class="btn" style="left:113px;top:591px;width:173px;height:41px">Request a Quote</div>
<svg class="abs" style="left:0;top:760px" width="1200" height="125" viewBox="0 0 1200 125" preserveAspectRatio="none">
  <path d="M0 125 L0 112 C140 40 300 20 520 60 C760 100 980 80 1200 20 L1200 125 Z" fill="#7b736a"/>
  <path d="M0 125 C200 60 380 70 600 95 C820 120 1000 90 1200 50 L1200 125 Z" fill="#4c9a40"/>
  <path d="M0 125 C220 85 420 95 620 110 C840 125 1020 105 1200 75 L1200 125 Z" fill="#fff"/>
</svg>

<!-- about -->
<h2 class="abs display" style="left:0;top:938px;width:1200px;text-align:center;font-size:34px">About us</h2>
<div class="title-rule" style="left:570px;top:993px"></div>
<p class="abs about-copy" style="top:1009px">Lorem Ipsum is simply dummy text of the printing and typesetting industryLorem Ipsum has been the<br>industry's standard dummy text ever since the 1500s.</p>
<p class="abs about-copy" style="top:1077px">when an unknown printer took a galley of type and scrambled it to make a type specimen book. It has<br>survived not only five centuries, but also the leap into electronic typesetting, remaining essentially unchanged.<br>It was popularised in the 1960s with the release of Letraset sheets containing and<br>more recently with desktop publishing software.</p>
<div class="btn" style="left:508px;top:1201px;width:172px;height:42px">Read More</div>

<!-- solution -->
<div class="abs solution-band"></div>
<h2 class="abs display" style="left:0;top:1386px;width:1200px;text-align:center;font-size:34px">Solution</h2>

<div class="card" style="left:74px;width:337px">
  <div class="photo" role="img" aria-label="Photograph of hands with a calculator and financial charts" style="background:linear-gradient(135deg,#dfe4ea,#9aa6b4)"></div>
  <div class="icon"><svg width="30" height="30" viewBox="0 0 30 30" fill="none" stroke="#4c9a40" stroke-width="1.6"><rect x="4" y="6" width="22" height="20" rx="2"/><path d="M4 12h22M10 3v6M20 3v6M9 17h4M17 17h4M9 21h4M17 21h4"/></svg></div>
  <h3 class="display">Tax and Accounting</h3><div class="rule"></div>
  <ul style="top:296px;line-height:28px"><li>Tax Compliance</li><li>IRD Investigations</li><li>Financial Reporting Compliance</li></ul>
  <div class="btn" style="left:20px;top:393px;width:137px;height:34px">Read More</div>
</div>

<div class="card" style="left:432px;width:336px">
  <div class="photo" role="img" aria-label="Photograph of a person counting banknotes over a desk" style="background:linear-gradient(135deg,#3a3a3a,#b9b2a3)"></div>
  <div class="icon"><svg width="30" height="30" viewBox="0 0 30 30" fill="none" stroke="#4c9a40" stroke-width="1.6"><path d="M15 3c4 4 5 9 4 15h-8c-1-6 0-11 4-15zM11 18l-4 5h6M19 18l4 5h-6M13 25h4"/><circle cx="15" cy="11" r="2"/></svg></div>
  <h3 class="display">Specialist</h3><div class="rule"></div>
  <ul><li>Business Startup,&nbsp; Buy-Sell</li><li>Asset Protection</li><li>Property Accounting</li><li>Cryptocurrency</li></ul>
  <div class="btn" style="left:18px;top:400px;width:137px;height:34px">Read More</div>
</div>

<div class="card" style="left:787px;width:337px">
  <div class="photo" role="img" aria-label="Photograph of a laptop with a data centre graphic" style="background:linear-gradient(135deg,#e8eef2,#8fb3c8)"></div>
  <div class="icon"><svg width="30" height="30" viewBox="0 0 30 30" fill="none" stroke="#4c9a40" stroke-width="1.6"><path d="M8 16a5 5 0 0 1 1-10 7 7 0 0 1 13 2 4 4 0 0 1 0 8z"/><rect x="5" y="17" width="12" height="9"/><path d="M8 20h6M8 23h6M20 20l5 5M25 20l-5 5"/></svg></div>
  <h3 class="display">Cloud Accounting</h3><div class="rule"></div>
  <ul style="line-height:27px"><li>Ledgerly</li><li>BookNest</li></ul>
  <div class="btn" style="left:18px;top:387px;width:137px;height:34px">Read More</div>
</div>

<!-- why choose us -->
<div class="abs why"></div>
<div class="abs" style="left:777px;top:2058px;width:423px;height:420px;background:var(--taupe)"></div>
<div class="abs" role="img" aria-label="Photograph of a hand writing over financial charts beside a calculator" style="left:632px;top:2077px;width:492px;height:380px;background:linear-gradient(135deg,#e9ecef,#b7c0ca 60%,#d9dde2)"></div>
<h2 class="abs display why-title">Why choose us</h2>
<div class="abs" style="left:74px;top:2122px;width:44px;height:2px;background:#fff"></div>
<ul class="abs why-list">
  <li><svg width="14" height="14" viewBox="0 0 14 14" fill="none" stroke="#fff" stroke-width="1.4"><circle cx="7" cy="7" r="6"/><path d="M4 7l2 2 4-4"/></svg>We specialise in accounting and tax solutions for all business structures and industries</li>
  <li><svg width="14" height="14" viewBox="0 0 14 14" fill="none" stroke="#fff" stroke-width="1.4"><circle cx="7" cy="7" r="6"/><path d="M4 7l2 2 4-4"/></svg>Our team are qualified professionals with 50+ years of combined experience in CA industry</li>
  <li><svg width="14" height="14" viewBox="0 0 14 14" fill="none" stroke="#fff" stroke-width="1.4"><circle cx="7" cy="7" r="6"/><path d="M4 7l2 2 4-4"/></svg>We are Accessable 7 days a week</li>
  <li><svg width="14" height="14" viewBox="0 0 14 14" fill="none" stroke="#fff" stroke-width="1.4"><circle cx="7" cy="7" r="6"/><path d="M4 7l2 2 4-4"/></svg>We constantly upskill to keep up with changes to tax laws and legislation</li>
  <li><svg width="14" height="14" viewBox="0 0 14 14" fill="none" stroke="#fff" stroke-width="1.4"><circle cx="7" cy="7" r="6"/><path d="M4 7l2 2 4-4"/></svg>Our advise is explained in plain english so you understand</li>
  <li><svg width="14" height="14" viewBox="0 0 14 14" fill="none" stroke="#fff" stroke-width="1.4"><circle cx="7" cy="7" r="6"/><path d="M4 7l2 2 4-4"/></svg>Our fees are not only fair but very competitive</li>
  <li><svg width="14" height="14" viewBox="0 0 14 14" fill="none" stroke="#fff" stroke-width="1.4"><circle cx="7" cy="7" r="6"/><path d="M4 7l2 2 4-4"/></svg>We don't believe in one size fits all, we listen to client's challenges indivually</li>
  <li><svg width="14" height="14" viewBox="0 0 14 14" fill="none" stroke="#fff" stroke-width="1.4"><circle cx="7" cy="7" r="6"/><path d="M4 7l2 2 4-4"/></svg>Our level of service and work ethics is no different to any other large CA practices</li>
  <li><svg width="14" height="14" viewBox="0 0 14 14" fill="none" stroke="#fff" stroke-width="1.4"><circle cx="7" cy="7" r="6"/><path d="M4 7l2 2 4-4"/></svg>We have affiliations with other business partners</li>
  <li><svg width="14" height="14" viewBox="0 0 14 14" fill="none" stroke="#fff" stroke-width="1.4"><circle cx="7" cy="7" r="6"/><path d="M4 7l2 2 4-4"/></svg>We keep up with everchanging cloud based technology</li>
</ul>

<!-- testimonials -->
<div class="abs" style="left:0;top:2629px;width:1200px;text-align:center;font-size:13px;color:#444">Testimonials</div>
<h2 class="abs display" style="left:0;top:2655px;width:1200px;text-align:center;font-size:34px">What clients say</h2>

<div class="quote-card" style="left:113px"><div class="quote-mark">“</div><div class="avatar" role="img" aria-label="Client portrait"></div><h4>CHRISTOPHER</h4><div class="role">Creative Director</div><p>Lorem Ipsum simply dummy text printing and typesetting industry simply dummy a psum is simply dummy</p><div class="stars">★★★★★</div></div>
<div class="quote-card" style="left:448px"><div class="quote-mark">“</div><div class="avatar" role="img" aria-label="Client portrait"></div><h4>SARAH ROSE</h4><div class="role">Creative Director</div><p>Lorem Ipsum simply dummy text printing and typesetting industry simply dummy a psum is simply dummy</p><div class="stars">★★★★★</div></div>
<div class="quote-card" style="left:783px"><div class="quote-mark">“</div><div class="avatar" role="img" aria-label="Client portrait"></div><h4>SAMANTHA JOHN</h4><div class="role">Creative Director</div><p>Lorem Ipsum simply dummy text printing and typesetting industry simply dummy a psum is simply dummy</p><div class="stars">★★★★★</div></div>

<svg class="abs" style="left:580px;top:3062px" width="40" height="10"><circle cx="6" cy="5" r="3.5" fill="#4c9a40"/><circle cx="19" cy="5" r="3.5" fill="#666"/><circle cx="32" cy="5" r="3.5" fill="#666"/></svg>

<!-- industries -->
<h2 class="abs display" style="left:0;top:3118px;width:1200px;text-align:center;font-size:34px">Industries we represent</h2>

<div class="ind" style="left:98px;top:3215px"><svg width="50" height="50" viewBox="0 0 50 50" fill="none" stroke="#4c9a40" stroke-width="2"><path d="M10 6v14a8 8 0 0 0 16 0V6M18 28v6a9 9 0 0 0 18 0v-6"/><circle cx="36" cy="25" r="4"/></svg>Healthcare<br>Specialists</div>
<div class="ind" style="left:386px;top:3215px"><svg width="50" height="50" viewBox="0 0 50 50" fill="none" stroke="#4c9a40" stroke-width="2"><path d="M6 8h30M12 8v38M6 46h38M20 24h20v22H20zM25 30h4M33 30h4M25 37h4M33 37h4"/></svg>Construction</div>
<div class="ind" style="left:654px;top:3215px"><svg width="50" height="50" viewBox="0 0 50 50" fill="none" stroke="#4c9a40" stroke-width="2"><circle cx="25" cy="18" r="7"/><path d="M25 6v4M25 26v4M13 18h4M33 18h4M6 40l10-6h14l-10 6M6 44h30l10-8"/></svg>Professional<br>Services</div>
<div class="ind" style="left:893px;top:3215px"><svg width="50" height="50" viewBox="0 0 50 50" fill="none" stroke="#4c9a40" stroke-width="2"><path d="M25 6v36M12 12h26M12 12l-6 14h12zM38 12l-6 14h12zM16 44h18"/></svg>Legal</div>

<div class="ind" style="left:98px;top:3303px"><svg width="50" height="50" viewBox="0 0 50 50" fill="none" stroke="#4c9a40" stroke-width="2"><path d="M14 18a11 11 0 0 1 22 0zM10 18h30M25 7v4M12 30h26v10H12zM18 30v10M32 30v10"/></svg>Contractors</div>
<div class="ind" style="left:386px;top:3303px"><svg width="50" height="50" viewBox="0 0 50 50" fill="none" stroke="#4c9a40" stroke-width="2"><path d="M8 8h34v34H8zM14 30l11-10 11 10v8H14zM22 38v-6h6v6"/></svg>Architecture</div>
<div class="ind" style="left:654px;top:3303px"><svg width="50" height="50" viewBox="0 0 50 50" fill="none" stroke="#4c9a40" stroke-width="2"><path d="M6 8h38v8H6zM9 16v28h32V16M14 24h10v20H14zM28 24h10v10H28z"/></svg>Retail</div>
<div class="ind" style="left:893px;top:3303px"><svg width="50" height="50" viewBox="0 0 50 50" fill="none" stroke="#4c9a40" stroke-width="2"><circle cx="25" cy="15" r="8"/><path d="M9 46c0-10 7-16 16-16s16 6 16 16M20 30v8M30 30v6"/></svg>Medical<br>Practioners</div>

<div class="ind" style="left:98px;top:3392px"><svg width="50" height="50" viewBox="0 0 50 50" fill="none" stroke="#4c9a40" stroke-width="2"><circle cx="12" cy="10" r="4"/><circle cx="25" cy="10" r="4"/><circle cx="38" cy="10" r="4"/><path d="M12 14v14M25 14v14M38 14v14M5 32h40v10H5zM11 37h2M20 37h2M29 37h2M38 37h2"/></svg>Manufacturing</div>
<div class="ind" style="left:386px;top:3392px"><svg width="50" height="50" viewBox="0 0 50 50" fill="none" stroke="#4c9a40" stroke-width="2"><path d="M5 24L25 8l20 16M10 20v24h30V20M20 44V32h10v12"/></svg>Real Estate<br>Rentals</div>
<div class="ind" style="left:654px;top:3392px"><svg width="50" height="50" viewBox="0 0 50 50" fill="none" stroke="#4c9a40" stroke-width="2"><circle cx="27" cy="12" r="5"/><path d="M20 30l7-10 7 10M6 38h10l10 4 16-8M6 44h12"/></svg>Childcare</div>
<div class="ind" style="left:893px;top:3392px"><svg width="50" height="50" viewBox="0 0 50 50" fill="none" stroke="#4c9a40" stroke-width="2"><path d="M6 20h38v24H6zM6 20l4-12 34 4-2 8M14 28h22M14 36h22"/></svg>Film Industry</div>

<!-- footer -->
<svg class="abs" style="left:0;top:3505px" width="1200" height="400" viewBox="0 0 1200 400" preserveAspectRatio="none">
  <path d="M0 60 C180 10 360 0 560 40 C760 80 960 70 1200 30 L1200 400 L0 400 Z" fill="#7b736a"/>
</svg>
<div class="footer">
  <div class="abs" style="left:74px;top:3712px;display:flex;align-items:center;gap:12px"><span style="width:22px;height:22px;background:#fff"></span><span style="font-size:19px;color:#fff;font-weight:500;letter-spacing:1px">LEDGERLINE ADVISORY</span></div>

  <h5 style="left:428px;top:3644px">Quick Links</h5><div class="hr" style="left:428px;top:3670px"></div>
  <ul style="left:428px;top:3688px"><li>Home</li><li>About us</li><li>Solution</li><li>Clients</li><li>Contact us</li><li>Clients Resource</li></ul>

  <h5 style="left:633px;top:3643px">Quick Contact</h5><div class="hr" style="left:633px;top:3669px"></div>
  <svg class="abs" style="left:608px;top:3693px" width="14" height="16" viewBox="0 0 14 16" fill="none" stroke="#fff" stroke-width="1.3"><path d="M7 15s5-5 5-9A5 5 0 0 0 2 6c0 4 5 9 5 9z"/><circle cx="7" cy="6" r="1.8"/></svg>
  <div class="contact" style="left:633px;top:3684px">P O Box 51720, Harbourview,<br>Kelston 4109</div>
  <svg class="abs" style="left:608px;top:3774px" width="14" height="12" viewBox="0 0 14 12" fill="none" stroke="#fff" stroke-width="1.2"><rect x="1" y="3" width="12" height="8" rx="1"/><path d="M3 3V1h8v2M5 7h4"/></svg>
  <div class="contact" style="left:633px;top:3766px">027 580 419</div>
  <svg class="abs" style="left:608px;top:3804px" width="14" height="11" viewBox="0 0 14 11" fill="none" stroke="#fff" stroke-width="1.2"><rect x="1" y="1" width="12" height="9"/><path d="M1 1l6 5 6-5"/></svg>
  <div class="contact" style="left:633px;top:3795px">hello@ledgerline.example</div>

  <h5 style="left:897px;top:3644px">Newsletter</h5><div class="hr" style="left:897px;top:3670px"></div>
  <div class="contact" style="left:897px;top:3687px;width:230px;line-height:15px;font-size:12px">Lorem Ipsum is simply dummy text and typesetting industry.</div>
  <div class="abs" style="left:897px;top:3738px;width:225px;height:34px;border-radius:17px;background:#fff;color:#888;font-size:12px;font-style:italic;padding:10px 18px">Your Email Address</div>
  <div class="btn" style="left:897px;top:3781px;width:225px;height:34px;font-size:11px">SUBSCRIBE</div>
</div>

<div class="abs" style="left:74px;top:3931px;font-size:12px;color:#333">Copyright © 2022 <b style="font-weight:600">LEDGERLINE ADVISORY</b>. All Rights Reserved</div>
<div class="abs" style="left:975px;top:3923px"><span class="social g"></span><span class="social"></span><span class="social"></span><span class="social"></span></div>

</body>
</html>
```